Missing Traveler Patterns: Seizures

Book cover. Casebound and Perfect bound. Size 5.5 x 8.5 (portrait). Approx 165 pages for spine. Will be using Corvel PressWorks for printer so be sure to follow those specifications. This is a textbook for Search & Rescue and Law Enforcement search planners on deciding where they should look for someone who has been abducted. Nothing morbid. It will be a book in a series. The series is called Missing Traveler Patterns. That should be in smaller letters at the top. Seizures should be the major title feature. The series will have a border on the front cover of safety orange (255, 121, 0) for RGB. hvQ logo on front, spine, and back. Place holder for ISBN, author bio, book description, endorsements on back.

Target Market(s)

Professional textbook for Law Enforcement, Search and Rescue, Academic (criminologist)

Industry/Entity Type

Search and Rescue - Law Enforcement. Major colors for industry is orange for SAR and blue for Law enforcement

Requirements
Must have
• Safety Orange border (0.25 inch), hvQ Logos, small Missing Traveler Patterns title on top, large Seizures title. Author's name (Daniel P. Marwick)
Nice to have
• Not sure if picture or illustration works best. Topographic map is possible, law enforcement and searcher working together, clandestine grave, dirt road, all possible
Should not have
• no dead bodies, no bones, no skulls, no urban environment

```html
<!DOCTYPE html>
<html lang="en">
<head>
<meta charset="utf-8">
<title>Missing Traveler Patterns: Seizures — Cover Wrap</title>
<link rel="stylesheet" href="https://fonts.googleapis.com/css2?family=Lato:wght@400;700&family=Oswald:wght@700&display=swap">
<style>
  :root {
    --safety-orange: #ff7900;
    --ink-black: #0d0f14;
    --night-navy: #0a1420;
    --paper-white: #ffffff;
  }
  * { margin: 0; padding: 0; box-sizing: border-box; }
  html, body { width: 1200px; height: 901px; overflow: hidden; }
  body {
    position: relative;
    background: var(--safety-orange);
    font-family: "Lato", Arial, sans-serif;
  }

  /* Back cover */
  .back-series {
    position: absolute; left: 0; width: 592px; top: 81px;
    text-align: center; color: var(--paper-white);
    font-size: 10.5px; font-weight: 700; letter-spacing: 2.2px;
    white-space: nowrap;
  }
  .back-title {
    position: absolute; left: 0; width: 592px; top: 90px;
    text-align: center; color: var(--ink-black);
    font-family: "Oswald", "Arial Narrow", sans-serif;
    font-weight: 700; font-size: 49px; line-height: 1.1;
  }
  .author-portrait {
    position: absolute; left: 62px; top: 528px; width: 104px; height: 104px;
    border-radius: 50%; border: 3px solid var(--paper-white);
    background: radial-gradient(circle at 50% 45%, #b9a08a 0%, #6d6a5e 55%, #3e4038 100%);
    box-shadow: 4px 6px 10px rgba(0,0,0,0.3);
  }
  .isbn-placeholder {
    position: absolute; left: 347px; top: 738px; width: 206px; height: 125px;
    background: var(--paper-white);
  }

  /* Publisher mark */
  .publisher-mark {
    position: absolute; display: flex; align-items: center; justify-content: center;
    background: var(--paper-white); border: 1px solid var(--ink-black);
    color: var(--ink-black); font-family: "Lato", Arial, sans-serif; font-weight: 700;
  }
  .publisher-mark--back { left: 62px; top: 762px; width: 68px; height: 53px; font-size: 28px; }
  .publisher-mark--spine { left: 587px; top: 762px; width: 26px; height: 20px; font-size: 11px; }
  .publisher-mark--front { left: 871px; top: 769px; width: 68px; height: 53px; font-size: 28px; }

  /* Spine */
  .spine-text {
    position: absolute; left: 609px; top: 190px;
    transform-origin: 0 0; transform: rotate(90deg);
    white-space: nowrap; color: var(--ink-black);
    font-size: 16.5px; font-weight: 400; letter-spacing: 0.2px;
  }
  .spine-text .spine-author { margin-left: 30px; }

  /* Front cover */
  .front-panel {
    position: absolute; left: 655px; top: 56px; width: 511px; height: 788px;
    background: var(--night-navy); overflow: hidden;
  }
  .front-art {
    position: absolute; inset: 0;
    background:
      radial-gradient(ellipse 34% 48% at 50% 48%, #c9cdd0 0%, #7f95ad 35%, #3b5370 70%, rgba(10,20,32,0) 100%),
      radial-gradient(ellipse at 50% 40%, #14263a 0%, var(--night-navy) 70%, #05090f 100%);
  }
  .front-series {
    position: absolute; left: 0; width: 100%; top: 40px;
    text-align: center; color: var(--paper-white);
    font-size: 21px; line-height: 1; font-weight: 700; letter-spacing: 3px;
    white-space: nowrap;
  }
  .front-title {
    position: absolute; left: 0; width: 100%; top: 62px;
    text-align: center; color: var(--safety-orange);
    font-family: "Oswald", "Arial Narrow", sans-serif;
    font-weight: 700; font-size: 92px; line-height: 1.1;
    white-space: nowrap;
  }
  .front-author {
    position: absolute; left: 0; width: 100%; top: 666px;
    text-align: center; color: var(--paper-white);
    font-size: 33px; font-weight: 700; letter-spacing: -0.5px;
    white-space: nowrap;
  }
</style>
</head>
<body>
  <section class="back-cover">
    <p class="back-series">MISSING TRAVELER PATTERNS</p>
    <h2 class="back-title">SEIZURES</h2>
    <div class="author-portrait" role="img" aria-label="Author portrait photograph"></div>
    <div class="isbn-placeholder" aria-label="ISBN placeholder"></div>
    <div class="publisher-mark publisher-mark--back">hvQ</div>
  </section>

  <section class="spine">
    <p class="spine-text">MISSING TRAVELER PATTERNS: SEIZURES<span class="spine-author">DANIEL P. MARWICK</span></p>
    <div class="publisher-mark publisher-mark--spine">hvQ</div>
  </section>

  <section class="front-panel">
    <div class="front-art" role="img" aria-label="Close-up photograph of a fingertip showing its fingerprint, lit in cold blue on a dark background"></div>
    <p class="front-series">MISSING TRAVELER PATTERNS</p>
    <h1 class="front-title">SEIZURES</h1>
    <p class="front-author">DANIEL P. MARWICK</p>
  </section>
  <div class="publisher-mark publisher-mark--front">hvQ</div>
</body>
</html>
```